Hospitality project presentation

I am developing a hospitality project and I need to present to the developer an outstanding presentation highlighting the overall look and feel. I will provide the text and most of the pictures (not all of them) some pictures (copyright free) will hae to be provided by the designer. Maximum number of pages 15, and zoom calls with me to make some adjustment if needed.

Industry/Entity Type

Hospitality

Font styles to use
Other font styles liked:
• calibri light

Requirements
Must have
• 15 slides
Nice to have
• Hospitality resort project look and feel

```html
<!DOCTYPE html>
<html lang="en">
<head>
<meta charset="utf-8">
<title>Hospitality Project Presentation – Slide Overview</title>
<link href="https://fonts.googleapis.com/css2?family=Hanken+Grotesk:wght@400;500;600;700;800&display=swap" rel="stylesheet">
<style>
  :root{
    --gold:#c8ad3a;
    --gold-deep:#b89c2c;
    --ink:#1d1d1d;
    --ink-2:#2b2b2b;
    --paper:#f4f4f2;
    --board:#545454;
    --white:#ffffff;
  }
  *{box-sizing:border-box;margin:0;padding:0}
  html,body{width:1200px;height:742px;overflow:hidden;background:var(--board)}
  body{font-family:"Hanken Grotesk",Arial,sans-serif;color:var(--ink)}
  .canvas{position:relative;width:1200px;height:742px;overflow:hidden;background:var(--board)}
  .board{position:absolute;left:0;top:0;width:1264px;height:782px;transform:scale(.9494);transform-origin:0 0}
  .slide{position:absolute;width:480px;height:270px;overflow:hidden;background:var(--paper)}
  .abs{position:absolute}
  .photo{position:absolute}
  .rule{position:absolute;height:12px}
  .rule svg{display:block}
  .slide-title{position:absolute;font-size:11.5px;font-weight:500;color:var(--gold);white-space:nowrap}
  .tag{position:absolute;background:var(--gold);color:var(--white);font-size:10.5px;font-weight:500;padding:2px 6px;white-space:nowrap}
  .footer{position:absolute;height:10px;background:var(--ink);color:#e6e6e6;font-size:5.5px;display:flex;align-items:center;justify-content:flex-end;padding-right:20px;white-space:nowrap}
  .footer b{font-weight:700}
  .footer .page{position:absolute;right:0;top:0;height:10px;width:16px;background:var(--gold);color:var(--ink);font-weight:700;display:flex;align-items:center;justify-content:center}
  .feat{position:absolute;display:flex;gap:6px;width:110px}
  .feat .ico{flex:0 0 12px;width:12px;height:12px}
  .feat h4{font-size:5.8px;font-weight:800;margin-bottom:2px;white-space:nowrap}
  .feat p{font-size:4.2px;line-height:1.4;font-weight:500;max-width:78px}
  .on-dark h4{color:var(--white)}
  .on-dark p{color:#dcdcdc}
  .price-item{position:absolute;display:flex;gap:6px;width:92px}
  .price-item .ico{flex:0 0 11px;width:11px;height:11px}
  .price-item h4{font-size:5.4px;font-weight:800;color:#fff;white-space:nowrap;line-height:1.1}
  .price-item p{font-size:3.8px;line-height:1.3;color:#d8d8d8;white-space:nowrap}
  .price{position:absolute;color:var(--gold);font-size:11.5px;font-weight:700;white-space:nowrap}
  .price small{font-size:5.5px;font-weight:500;vertical-align:top}
  .para{font-size:4.6px;line-height:1.45;color:#e4e4e4;font-weight:500}
  .c-feat{position:absolute;display:flex;gap:6px;color:#fff;font-size:5.6px;font-weight:600;line-height:1.3}
  .c-feat svg{flex:0 0 11px}
</style>
</head>
<body>
<div class="canvas">
<div class="board">

  <!-- Row 1 -->
  <section class="slide" style="left:-390px;top:-23px;background:#e8e8e6">
    <div class="abs" style="left:390px;top:23px;width:60px;height:58px;background:var(--gold);color:#fff;font-size:11px;line-height:1.3;padding:0 0 8px 2px;display:flex;align-items:flex-end;white-space:nowrap">allery<br>Grid +<br>Text</div>
    <div class="photo" role="img" aria-label="Close-up of light oak timber steps" style="left:390px;top:135px;width:55px;height:102px;background:linear-gradient(168deg,#e9e5df 0%,#cdb7a0 30%,#a87d57 58%,#8d6444 80%,#c49c78 100%)"></div>
  </section>

  <section class="slide" style="left:105px;top:-23px;background:#fafafa">
    <div class="photo" role="img" aria-label="Dim interior hallway with dark timber floor" style="left:0;top:0;width:205px;height:270px;background:radial-gradient(ellipse at 70% 35%,rgba(120,110,98,.45),rgba(0,0,0,0) 55%),linear-gradient(180deg,#2a2a2a 0%,#1e1e1e 55%,#3a2e24 80%,#2a221c 100%)"></div>
    <div class="rule" style="left:42px;top:38px"><svg width="410" height="12"><polyline points="0,11 18,2 36,11 410,11" fill="none" stroke="var(--gold)" stroke-width=".8"/></svg></div>
    <div class="slide-title" style="right:30px;top:33px">Project Rationale</div>
    <div class="abs" style="left:40px;top:88px;width:80px;color:var(--gold);font-size:6.6px;font-weight:800;line-height:1.3">Lorem ipsum dolor sit amet, consectetur adipiscing elit. Mauris ipsum odio, vehicula ac venenatis at, maximus in dolor.</div>
    <p class="abs para" style="left:40px;top:146px;width:78px">Vestibulum porta justo quis suscipit tempus. Curabitur turpis libero, venenatis tincidunt neque.</p>
    <p class="abs para" style="left:40px;top:180px;width:78px">Phasellus cursus nisi at libero fringilla, elementum mi euismod. Donec lacinia arcu.</p>
    <div class="feat" style="left:242px;top:90px"><svg class="ico" viewBox="0 0 12 12"><rect x="1" y="3" width="10" height="8" rx="1.5" fill="var(--gold)"/><rect x="4" y="1" width="4" height="3" fill="none" stroke="var(--gold)"/></svg><div><h4>Sed luctus luctus posuere.</h4><p>Pellentesque habitant morbi tristique senectus et netus et malesuada fames ac turpis egestas. Vestibulum velit lacus, pharetra quis.</p></div></div>
    <div class="feat" style="left:357px;top:90px"><svg class="ico" viewBox="0 0 12 12"><rect x="3" y="1" width="6" height="10" rx="1" fill="var(--gold)"/></svg><div><h4>Sed luctus luctus posuere.</h4><p>Pellentesque habitant morbi tristique senectus et netus et malesuada fames ac turpis egestas. Vestibulum velit lacus, pharetra quis.</p></div></div>
    <div class="feat" style="left:242px;top:136px"><svg class="ico" viewBox="0 0 12 12"><path d="M2 1v10M2 1h8l-2 3 2 3H2" fill="var(--gold)" stroke="var(--gold)"/></svg><div><h4>Sed luctus luctus posuere.</h4><p>Pellentesque habitant morbi tristique senectus et netus et malesuada fames ac turpis egestas. Vestibulum velit lacus, pharetra quis.</p></div></div>
    <div class="feat" style="left:357px;top:136px"><svg class="ico" viewBox="0 0 12 12"><rect x="1" y="2" width="10" height="9" rx="1.5" fill="var(--gold)"/><rect x="3" y="5" width="2" height="2" fill="#fff"/><rect x="7" y="5" width="2" height="2" fill="#fff"/></svg><div><h4>Sed luctus luctus posuere.</h4><p>Pellentesque habitant morbi tristique senectus et netus et malesuada fames ac turpis egestas. Vestibulum velit lacus, pharetra quis.</p></div></div>
    <div class="feat" style="left:242px;top:180px"><svg class="ico" viewBox="0 0 12 12"><circle cx="6" cy="6" r="5.5" fill="var(--gold)"/><text x="6" y="8.5" font-size="7" fill="#fff" text-anchor="middle" font-family="Arial">?</text></svg><div><h4>Sed luctus luctus posuere.</h4><p>Pellentesque habitant morbi tristique senectus et netus et malesuada fames ac turpis egestas. Vestibulum velit lacus, pharetra quis.</p></div></div>
    <div class="feat" style="left:357px;top:180px"><svg class="ico" viewBox="0 0 12 12"><circle cx="6" cy="6" r="4" fill="none" stroke="var(--gold)" stroke-width="2.4" stroke-dasharray="2 1.2"/><circle cx="6" cy="6" r="2" fill="var(--gold)"/></svg><div><h4>Sed luctus luctus posuere.</h4><p>Pellentesque habitant morbi tristique senectus et netus et malesuada fames ac turpis egestas. Vestibulum velit lacus, pharetra quis.</p></div></div>
    <div class="footer" style="left:205px;top:253px;width:275px">Sample Hospitality Powerpoint &gt;&nbsp;<b>Introduction</b><span class="page">01</span></div>
  </section>

  <section class="slide" style="left:600px;top:-23px;background:#fafafa">
    <div class="rule" style="left:32px;top:28px"><svg width="260" height="12"><polyline points="0,11 16,2 32,11 260,11" fill="none" stroke="var(--gold)" stroke-width=".8"/></svg></div>
    <div class="photo" role="img" aria-label="Floor plan of the residence" style="left:52px;top:58px;width:186px;height:178px;background:radial-gradient(ellipse at 50% 45%,#cfcfcf 0%,#e2e2e2 45%,#f6f6f6 75%,#fafafa 100%)"></div>
    <div class="abs" style="left:283px;top:0;width:160px;height:198px;background:var(--ink-2);padding:34px 14px 0 14px">
      <div style="color:var(--gold);font-size:11.5px;font-weight:500;margin-bottom:10px;white-space:nowrap">Location/Map/Plan</div>
      <p class="para" style="margin-bottom:6px">Pellentesque habitant morbi tristique senectus et netus et malesuada fames ac turpis egestas. Sed ac lacinia mauris. Proin nisl odio, pellentesque quis nulla eget, laoreet malesuada ipsum.</p>
      <p class="para" style="margin-bottom:6px">Vestibulum velit lacus, pharetra quis faucibus nec, pharetra eu est. Duis et libero tortor. Fusce sit amet tincidunt tortor, quis pharetra augue. Nulla lobortis porta, semper quam nec, iaculis lacus.</p>
      <p class="para">Nulla porta turpis sed nisi euismod, quis elementum tellus facilisis. Mauris sed nunc et nulla varius malesuada. Sed luctus lacus posuere.</p>
    </div>
    <div class="abs" style="left:32px;top:246px;font-size:8px;font-weight:800;color:var(--ink);letter-spacing:.2px;white-space:nowrap">Casa Lumen</div>
    <div class="footer" style="left:283px;top:253px;width:197px">Sample Hospitality Powerpoint &gt;&nbsp;<b>Large Graphic</b><span class="page">03</span></div>
  </section>

  <section class="slide" style="left:1095px;top:-23px">
    <div class="photo" role="img" aria-label="Bright bathroom with white tiles and glass shower" style="left:0;top:0;width:480px;height:270px;background:radial-gradient(ellipse at 25% 30%,#ffffff 0%,rgba(255,255,255,0) 50%),linear-gradient(100deg,#c9ced2 0%,#eef0f1 30%,#dfe2e4 55%,#b9bec3 80%,#d7dadc 100%)"></div>
    <div class="abs" style="left:40px;top:140px;width:200px;height:93px;background:rgba(255,255,255,.92)"></div>
    <div class="feat" style="left:55px;top:165px;width:160px"><svg class="ico" viewBox="0 0 12 12"><circle cx="6" cy="6" r="5.5" fill="var(--gold)"/><path d="M7 3.5L4.5 6 7 8.5" stroke="#fff" fill="none"/></svg><div><h4>Sed luctus luctus posuere.</h4><p style="max-width:110px">Pellentesque habitant morbi tristique senectus et netus et malesuada.</p></div></div>
    <div class="feat" style="left:55px;top:200px;width:160px"><svg class="ico" viewBox="0 0 12 12"><circle cx="6" cy="6" r="4" fill="none" stroke="var(--gold)" stroke-width="2.4" stroke-dasharray="2 1.2"/><circle cx="6" cy="6" r="2" fill="var(--gold)"/></svg><div><h4>Sed luctus luctus posuere.</h4><p style="max-width:110px">Pellentesque habitant morbi tristique senectus et netus et malesuada.</p></div></div>
  </section>

  <!-- Row 2 -->
  <section class="slide" style="left:-390px;top:262px">
    <div class="photo" role="img" aria-label="Kitchen with white cabinets and timber island" style="left:0;top:0;width:480px;height:270px;background:radial-gradient(ellipse at 88% 80%,#6b4429 0%,rgba(107,68,41,0) 30%),linear-gradient(170deg,#f2f0ec 0%,#dcd8d1 40%,#b7b0a5 65%,#8a6a4c 85%,#5e3f28 100%)"></div>
    <div class="tag" style="left:385px;top:33px">Half Image B</div>
    <div class="footer" style="left:360px;top:253px;width:120px">Powerpoint &gt;&nbsp;<b>Introduction</b><span class="page">01</span></div>
  </section>

  <section class="slide" style="left:105px;top:262px;background:#f1f1f1">
    <div class="photo" role="img" aria-label="Wooden hourglass against a painted brick wall, tinted gold" style="left:15px;top:15px;width:450px;height:255px;background:radial-gradient(ellipse 22% 55% at 56% 55%,#bb9a45 0%,#c6a84a 45%,rgba(200,173,58,0) 100%),linear-gradient(90deg,#c7ab3a 0%,#d1b650 50%,#c0a536 100%)"></div>
    <div class="abs" style="left:115px;top:122px;color:#fff;font-size:19px;font-weight:700;letter-spacing:2.5px">BREAK</div>
    <div class="abs" style="left:15px;top:225px;width:450px;height:45px;background:rgba(120,100,20,.28);display:flex;align-items:center;color:#fff;font-size:6.6px;font-weight:500;white-space:nowrap">
      <div style="display:flex;align-items:center;gap:6px;padding:0 16px 0 22px;border-right:1px solid rgba(255,255,255,.5);height:26px"><svg width="12" height="12" viewBox="0 0 12 12"><path d="M6 1a3.5 3.5 0 0 1 3.5 3.5C9.5 7 6 11 6 11S2.5 7 2.5 4.5A3.5 3.5 0 0 1 6 1z" fill="none" stroke="#fff"/><circle cx="6" cy="4.5" r="1.2" fill="#fff"/></svg><span>Lindenweg 24<br>8045 Talberg</span></div>
      <div style="display:flex;align-items:center;gap:6px;padding:0 16px"><svg width="12" height="12" viewBox="0 0 12 12"><circle cx="6" cy="6" r="5.5" fill="none" stroke="#fff"/><rect x="3" y="4" width="6" height="4" fill="none" stroke="#fff" stroke-width=".8"/><path d="M3 4l3 2 3-2" fill="none" stroke="#fff" stroke-width=".8"/></svg>hello@casalumen.ch</div>
      <div style="display:flex;align-items:center;gap:6px;padding:0 0 0 30px"><svg width="12" height="12" viewBox="0 0 12 12"><circle cx="6" cy="6" r="5.5" fill="none" stroke="#fff"/><path d="M4 3.5c0 3 1.5 4.5 4.5 4.5l.3-1.2-1.3-.6-.6.7c-.8-.4-1.3-.9-1.7-1.7l.7-.6-.6-1.3z" fill="#fff"/></svg>+41 55 210 34 70</div>
      <div style="margin-left:auto;padding-right:20px">www.casalumen.ch</div>
    </div>
  </section>

  <section class="slide" style="left:600px;top:262px">
    <div class="photo" role="img" aria-label="Bedroom with ceiling fan, dark dresser and grey bedding" style="left:0;top:0;width:480px;height:270px;background:radial-gradient(ellipse 30% 22% at 62% 42%,#2a2623 0%,rgba(42,38,35,0) 100%),radial-gradient(ellipse 45% 30% at 25% 75%,#8c95a3 0%,rgba(140,149,163,0) 100%),linear-gradient(180deg,#eceae6 0%,#e2dfd9 35%,#cfcac2 55%,#9b958d 78%,#6c6760 100%)"></div>
    <div class="rule" style="left:35px;top:38px"><svg width="410" height="12"><polyline points="0,11 18,2 36,11 410,11" fill="none" stroke="#fff" stroke-width=".8"/></svg></div>
    <div class="tag" style="left:380px;top:31px">Full Image B</div>
    <div class="abs" style="left:318px;top:131px;width:157px;height:118px;background:rgba(60,60,60,.6)"></div>
    <div class="feat on-dark" style="left:336px;top:153px;width:130px"><svg class="ico" viewBox="0 0 12 12"><circle cx="6" cy="6" r="5.5" fill="var(--gold)"/><path d="M7 3.5L4.5 6 7 8.5" stroke="#fff" fill="none"/></svg><div><h4>Sed luctus luctus posuere.</h4><p style="max-width:105px">Pellentesque habitant morbi tristique senectus et netus et malesuada.</p></div></div>
    <div class="feat on-dark" style="left:336px;top:190px;width:130px"><svg class="ico" viewBox="0 0 12 12"><circle cx="6" cy="6" r="4" fill="none" stroke="var(--gold)" stroke-width="2.4" stroke-dasharray="2 1.2"/><circle cx="6" cy="6" r="2" fill="var(--gold)"/></svg><div><h4>Sed luctus luctus posuere.</h4><p style="max-width:105px">Pellentesque habitant morbi tristique senectus et netus et malesuada.</p></div></div>
    <div class="footer" style="left:288px;top:253px;width:192px">Sample Hospitality Powerpoint &gt;&nbsp;<b>Introduction</b><span class="page">01</span></div>
  </section>

  <section class="slide" style="left:1095px;top:262px;background:#050505">
    <div class="abs" style="left:3px;top:34px;width:127px;height:99px;background:var(--gold);color:#fff;font-size:11px;line-height:1.4;display:flex;align-items:center;justify-content:center;text-align:center">Gallery<br>Grid+Text</div>
    <div class="photo" role="img" aria-label="Hotel room with upholstered headboard" style="left:133px;top:34px;width:120px;height:99px;background:linear-gradient(160deg,#4d443c 0%,#7b6d60 45%,#a8978a 100%)"></div>
    <div class="photo" role="img" aria-label="Bedside table with lamp" style="left:30px;top:138px;width:100px;height:100px;background:radial-gradient(ellipse at 70% 30%,#e9e1d2 0%,rgba(233,225,210,0) 55%),linear-gradient(180deg,#cfc6b8 0%,#a69b8c 50%,#3a2f27 75%,#8a7a68 100%)"></div>
    <div class="photo" role="img" aria-label="Neutral bedroom interior" style="left:133px;top:138px;width:120px;height:100px;background:linear-gradient(160deg,#e3dbcd 0%,#c7b9a5 50%,#8c7b68 100%)"></div>
  </section>

  <!-- Row 3 -->
  <section class="slide" style="left:-390px;top:546px">
    <div class="photo" role="img" aria-label="Stone house exterior with a metal roof under a blue sky" style="left:0;top:0;width:480px;height:270px;background:linear-gradient(180deg,#5d8fcf 0%,#9fc3ea 35%,#5f7386 50%,#e2ddd2 62%,#c9bfae 82%,#8f8a78 100%)"></div>
    <div class="abs" style="left:393px;top:35px;color:#fff;font-size:11.5px;font-weight:500;border-bottom:1px solid #fff;padding-bottom:2px;white-space:nowrap">Our Profile</div>
  </section>

  <section class="slide" style="left:105px;top:546px;background:#fafafa">
    <div class="abs" style="left:0;top:117px;width:480px;height:153px;background:#0e0e0e"></div>
    <div class="rule" style="left:50px;top:32px"><svg width="400" height="12"><polyline points="0,11 18,2 36,11 400,11" fill="none" stroke="var(--gold)" stroke-width=".8"/></svg></div>
    <div class="slide-title" style="right:30px;top:28px">Pricing/Options</div>

    <div class="photo" role="img" aria-label="Dining area beside a bright window" style="left:80px;top:78px;width:80px;height:64px;background:radial-gradient(ellipse at 35% 30%,#ffffff 0%,rgba(255,255,255,0) 60%),linear-gradient(160deg,#eef0f0 0%,#c9c6bf 55%,#8e8a82 100%)"></div>
    <div class="photo" role="img" aria-label="Kitchen sink and marble counter" style="left:210px;top:78px;width:80px;height:64px;background:linear-gradient(170deg,#e8e8e5 0%,#bdbab3 55%,#74706a 100%)"></div>
    <div class="photo" role="img" aria-label="Kitchen with grey cabinetry" style="left:340px;top:78px;width:80px;height:64px;background:linear-gradient(170deg,#ecebe8 0%,#b2aea7 50%,#6d6a64 100%)"></div>

    <svg class="abs" style="left:69px;top:67px" width="22" height="22"><circle cx="11" cy="11" r="10" fill="var(--gold)"/><text x="11" y="15" font-size="10" font-weight="700" fill="#fff" text-anchor="middle" font-family="Hanken Grotesk,Arial">A</text></svg>
    <svg class="abs" style="left:199px;top:67px" width="22" height="22"><circle cx="11" cy="11" r="10" fill="var(--gold)"/><text x="11" y="15" font-size="10" font-weight="700" fill="#fff" text-anchor="middle" font-family="Hanken Grotesk,Arial">B</text></svg>
    <svg class="abs" style="left:329px;top:67px" width="22" height="22"><circle cx="11" cy="11" r="10" fill="var(--gold)"/><text x="11" y="15" font-size="10" font-weight="700" fill="#fff" text-anchor="middle" font-family="Hanken Grotesk,Arial">C</text></svg>

    <div class="price-item" style="left:78px;top:150px"><svg class="ico" viewBox="0 0 12 12"><path d="M11 1L1 5l4 2 2 4z" fill="var(--gold)"/></svg><div><h4>Sed luctus luctus posuere</h4><p>Pellentesque habitant morbi tristique<br>senectus et netus et malesu</p></div></div>
    <div class="price-item" style="left:78px;top:168px"><svg class="ico" viewBox="0 0 12 12"><rect x="1" y="2" width="4" height="9" fill="var(--gold)"/><rect x="6" y="4" width="5" height="7" fill="var(--gold)"/></svg><div><h4>Sed luctus luctus posuere</h4><p>Pellentesque habitant morbi tristique<br>senectus et netus et malesu</p></div></div>
    <div class="price-item" style="left:78px;top:186px"><svg class="ico" viewBox="0 0 12 12"><path d="M5 2L1 6l4 4V7.5c3 0 5 1 6 3.5 0-4-2.5-6.5-6-6.5z" fill="var(--gold)"/></svg><div><h4>Sed luctus luctus posuere</h4><p>Pellentesque habitant morbi tristique<br>senectus et netus et malesu</p></div></div>

    <div class="price-item" style="left:208px;top:150px"><svg class="ico" viewBox="0 0 12 12"><path d="M11 1L1 5l4 2 2 4z" fill="var(--gold)"/></svg><div><h4>Sed luctus luctus posuere</h4><p>Pellentesque habitant morbi tristique<br>senectus et netus et malesu</p></div></div>
    <div class="price-item" style="left:208px;top:168px"><svg class="ico" viewBox="0 0 12 12"><rect x="1" y="2" width="4" height="9" fill="var(--gold)"/><rect x="6" y="4" width="5" height="7" fill="var(--gold)"/></svg><div><h4>Sed luctus luctus posuere</h4><p>Pellentesque habitant morbi tristique<br>senectus et netus et malesu</p></div></div>
    <div class="price-item" style="left:208px;top:186px"><svg class="ico" viewBox="0 0 12 12"><path d="M5 2L1 6l4 4V7.5c3 0 5 1 6 3.5 0-4-2.5-6.5-6-6.5z" fill="var(--gold)"/></svg><div><h4>Sed luctus luctus posuere</h4><p>Pellentesque habitant morbi tristique<br>senectus et netus et malesu</p></div></div>

    <div class="price-item" style="left:338px;top:150px"><svg class="ico" viewBox="0 0 12 12"><path d="M11 1L1 5l4 2 2 4z" fill="var(--gold)"/></svg><div><h4>Sed luctus luctus posuere</h4><p>Pellentesque habitant morbi tristique<br>senectus et netus et malesu</p></div></div>
    <div class="price-item" style="left:338px;top:168px"><svg class="ico" viewBox="0 0 12 12"><rect x="1" y="2" width="4" height="9" fill="var(--gold)"/><rect x="6" y="4" width="5" height="7" fill="var(--gold)"/></svg><div><h4>Sed luctus luctus posuere</h4><p>Pellentesque habitant morbi tristique<br>senectus et netus et malesu</p></div></div>
    <div class="price-item" style="left:338px;top:186px"><svg class="ico" viewBox="0 0 12 12"><path d="M5 2L1 6l4 4V7.5c3 0 5 1 6 3.5 0-4-2.5-6.5-6-6.5z" fill="var(--gold)"/></svg><div><h4>Sed luctus luctus posuere</h4><p>Pellentesque habitant morbi tristique<br>senectus et netus et malesu</p></div></div>

    <div class="abs" style="left:78px;top:207px;width:90px;border-top:1px solid var(--gold)"></div>
    <div class="abs" style="left:208px;top:207px;width:90px;border-top:1px solid var(--gold)"></div>
    <div class="abs" style="left:338px;top:207px;width:90px;border-top:1px solid var(--gold)"></div>
    <div class="price" style="left:108px;top:212px">€1230<small> /night</small></div>
    <div class="price" style="left:238px;top:212px">€2345<small> /night</small></div>
    <div class="price" style="left:368px;top:212px">€3450<small> /night</small></div>
  </section>

  <section class="slide" style="left:600px;top:546px;background:var(--gold)">
    <div class="photo" role="img" aria-label="Faint view of a house exterior tinted gold" style="left:0;top:0;width:480px;height:270px;background:radial-gradient(ellipse 55% 35% at 62% 50%,rgba(255,255,255,.13),rgba(255,255,255,0) 100%),linear-gradient(180deg,#c9ae3c 0%,#c5a938 55%,#bca132 100%)"></div>
    <div class="rule" style="left:40px;top:36px"><svg width="410" height="12"><polyline points="0,11 18,2 36,11 410,11" fill="none" stroke="#fff" stroke-width=".8"/></svg></div>
    <div class="abs" style="right:20px;top:33px;color:#fff;font-size:11.5px;font-weight:500;white-space:nowrap">Features Type C</div>
    <div class="abs" style="left:60px;top:60px;width:240px;height:64px;border:1px solid rgba(255,255,255,.85)"></div>
    <div class="abs" style="left:75px;top:85px;color:#fff;font-size:8.6px;font-weight:700;line-height:1.25">Lorem ipsum dolor<br>sit, amet aussi</div>
    <svg class="abs" style="left:196px;top:78px" width="74" height="32" viewBox="0 0 74 32"><circle cx="16" cy="16" r="14" fill="none" stroke="#fff" stroke-opacity=".8" stroke-width="1.2"/><path d="M16 16V2a14 14 0 0 1 14 14z" fill="#fff" fill-opacity=".8"/><rect x="42" y="18" width="6" height="12" fill="#fff" fill-opacity=".8"/><rect x="51" y="10" width="6" height="20" fill="#fff" fill-opacity=".8"/><rect x="60" y="4" width="6" height="26" fill="#fff" fill-opacity=".8"/></svg>
    <div class="abs" style="left:200px;top:124px;width:0;height:80px;border-left:1px dotted rgba(255,255,255,.7)"></div>
    <div class="abs" style="left:315px;top:96px;width:0;height:110px;border-left:1px dotted rgba(255,255,255,.7)"></div>

    <div class="c-feat" style="left:88px;top:140px"><svg width="11" height="11" viewBox="0 0 12 12"><circle cx="6" cy="4" r="2.5" fill="#fff" fill-opacity=".8"/><path d="M1.5 11c0-3 2-4.5 4.5-4.5s4.5 1.5 4.5 4.5z" fill="#fff" fill-opacity=".8"/></svg><span>Consectetur adipiscing elit</span></div>
    <div class="c-feat" style="left:88px;top:166px"><svg width="11" height="11" viewBox="0 0 12 12"><rect x="1" y="2" width="10" height="9" rx="1.5" fill="#fff" fill-opacity=".8"/></svg><span>Mauris ipsum odio,<br>vehicula ac venenatis</span></div>
    <div class="c-feat" style="left:88px;top:194px"><svg width="11" height="11" viewBox="0 0 12 12"><rect x="1" y="3" width="10" height="8" rx="1.5" fill="#fff" fill-opacity=".8"/></svg><span>Vivamus euismod<br>venenatis aliquam</span></div>
    <div class="c-feat" style="left:208px;top:140px"><svg width="11" height="11" viewBox="0 0 12 12"><path d="M3 1h6v3a3 3 0 0 1-6 0zM5 8h2v2h2v1H3v-1h2z" fill="#fff" fill-opacity=".8"/></svg><span>Maecenas posuere consequat</span></div>
    <div class="c-feat" style="left:208px;top:166px"><svg width="11" height="11" viewBox="0 0 12 12"><path d="M2 10l4-8 4 8z" fill="#fff" fill-opacity=".8"/></svg><span>Aenean eget vehicula</span></div>
    <div class="c-feat" style="left:208px;top:190px"><svg width="11" height="11" viewBox="0 0 12 12"><circle cx="6" cy="6" r="4.5" fill="#fff" fill-opacity=".8"/></svg><span>Sed dignissim<br>nunc vitae fringilla</span></div>
    <div class="c-feat" style="left:325px;top:106px"><svg width="11" height="11" viewBox="0 0 12 12"><path d="M6 11S1 7.5 1 4.5A2.5 2.5 0 0 1 6 3a2.5 2.5 0 0 1 5 1.5C11 7.5 6 11 6 11z" fill="#fff" fill-opacity=".8"/></svg><span>Mauris ipsum odio, vehicula<br>ac venenatis at, maximus in<br>dolor posuere</span></div>
    <div class="c-feat" style="left:325px;top:140px"><svg width="11" height="11" viewBox="0 0 12 12"><rect x="1" y="2" width="10" height="9" rx="1.5" fill="#fff" fill-opacity=".8"/></svg><span>Maecenas posuere consequ<br>at luctus sed faucibus. Sed<br>dignissim nunc vitae</span></div>
    <div class="c-feat" style="left:325px;top:174px"><svg width="11" height="11" viewBox="0 0 12 12"><path d="M6 1l1.5 3.2 3.5.4-2.6 2.4.7 3.5L6 8.8 2.9 10.5l.7-3.5L1 4.6l3.5-.4z" fill="#fff" fill-opacity=".8"/></svg><span>Sed ac maximus diam. Nulla<br>pulvinar purus et congue<br>tincidunt. Aenean eget aliqu<br>vehicula pharetra</span></div>
  </section>

  <section class="slide" style="left:1095px;top:546px;background:#f3f3f3">
    <div class="photo" role="img" aria-label="Stone house exterior with trees and blue sky" style="left:13px;top:16px;width:467px;height:254px;background:linear-gradient(180deg,#4f82c2 0%,#8db6e2 40%,#b8cde0 52%,#6c7a6a 60%,#e0dbcf 70%,#bfb39c 85%,#9c8e74 100%)"></div>
    <div class="abs" style="left:63px;top:69px;color:#fff;font-size:19px;font-weight:700;letter-spacing:1.6px;white-space:nowrap">THANK YOU</div>
  </section>

</div>
</div>
</body>
</html>
```